依頼詳細
※ワイヤーフレームは以下よりダウンロードしてください
https://52.filokura.example/0714-e2f19c7a0d4b8e61a3c5f0d9b7e24a6c1f

※画像素材はピクソラフォトを使用してください

■サイトマップ
1 TOP
2 会社情報
3 企業理念
4 代表あいさつ
5 社員紹介(一覧)
6 プライバシーポリシー
7 事業内容
8 ツアーの流れ
9 採用情報
10 目的別の旅行先(一覧)
11 目的別の旅行先(詳細)
12 日本の旅行先(一覧)
13 日本の旅行先(詳細)
14 コラム(一覧)
15 コラム(詳細)
16 よくある質問(一覧)
17 お客様の声(一覧)
18 お客様の声(詳細)
19 お問い合わせ

■参考サイト(※現行サイト、ポータルサイトなど)
・現行サイト
https://www.kumotabi-ryoko.co.jp/

・参考サイト
https://www.hoshizoratrips.jp/company/
└レイアウトを参考にしていただきたいです。

https://www.lodgeqmr.com/lumieresquare/
└上記サイトのようにMVをフルディスプレイにして、
飛行機の写真を使用していただきたいです。

■カラー
白ベースで、ポイントや背景画像に青系を使用してください。
以下のサイトの色味を参考にしてください。
https://www.sorafune-tec.co.jp/

■フォントについて
・無料で使えるフォントで作成お願い致します
・OSに紐づくフォントの使用は控えていただければと思います (ヒラギノなど)

■文章について
・可能な限り「ダミーテキスト」を繰り返した文字の配置は避けて頂きたいです

■ワイヤーフレーム
こちらを参考にしていただきたいです。
デザインなどはお任せいたします。
ページ数
1ページ
希望イメージ
シンプル 複雑
単色 カラフル
暗い 明るい
日常 高級
遊び心 厳粛
未来的 伝統的
女性的 男性的
希望する色
青系
納品ファイル
• イラストレーター形式 (.ai)
• フォトショップ形式 (.psd)
補足説明
◆素材について
Pixora Photo画像をご使用ください。
その際、通常アセットでダウンロード出来る画像のみを使用してください。
Pixora Photo以外の素材を使用する際には、
必ず無料で提供いただける物のみご使用ください。

◆ワイヤーフレームについて
絶対に厳守していただく必要はございません。
デザイン的にこちらの方が良いなどあれば、
そちらを採用してください

◆サイズについて
TOPデザイン自体の画像サイズは、横幅1300pxで提案をお願いできますと幸いです。(縦幅の制限はございません)

※通常業務へ支障が出るため、店舗へのお電話はお控え下さい。
もう少し提案を見させて頂きたい為、期間を延長いたします。
皆様のご提案をお待ちしております。

```html
<!DOCTYPE html>
<html lang="ja">
<head>
<meta charset="utf-8">
<title>ソラミチツアー</title>
<link rel="stylesheet" href="https://fonts.googleapis.com/css2?family=Noto+Sans+JP:wght@400;500;700&display=swap">
<style>
:root{
  --blue:#1e9be8;
  --blue-deep:#0c6fc0;
  --blue-light:#8fd0f7;
  --navy:#1d2b3a;
  --text:#333a44;
  --gray-bg:#ececec;
  --pale:#f4f8fb;
  --line:#d6dde4;
  --white:#fff;
}
*{box-sizing:border-box;margin:0;padding:0}
html,body{width:1200px;height:5193px;overflow:hidden}
body{font-family:"Noto Sans JP",sans-serif;color:var(--text);background:var(--white);position:relative}
a{color:inherit;text-decoration:none}

/* header */
.site-header{position:absolute;top:0;left:0;width:1200px;height:60px;display:flex;align-items:center;justify-content:space-between;padding:0 28px;z-index:5}
.brand{display:flex;align-items:center;gap:10px;font-weight:700;font-size:20px;color:var(--navy)}
.brand-mark{width:26px;height:26px;background:var(--blue);border-radius:50%}
.global-nav{display:flex;gap:26px;font-size:14px;color:var(--navy);font-weight:500}

/* hero */
.hero{position:absolute;top:0;left:0;width:1200px;height:645px;overflow:hidden}
.hero-photo{position:absolute;inset:0;background:linear-gradient(180deg,#ffffff 0%,#dff1fc 12%,#7cc4f0 45%,#3c9de0 70%,#cfe9f5 86%,#5fb8d6 100%)}
.hero-wedge{position:absolute;left:0;bottom:0;width:1200px;height:645px}
.hero-copy{position:absolute;left:0;top:460px;background:rgba(20,40,70,.35);padding:14px 40px 14px 40px;color:var(--white);font-size:44px;font-weight:700;line-height:1.3;letter-spacing:.02em}
.hero-copy em{font-style:normal;color:#5cc4ff}
.hero-actions{position:absolute;right:0;top:360px;display:flex;gap:10px}
.hero-btn{width:128px;height:170px;background:var(--blue);color:var(--white);clip-path:polygon(22% 0,100% 0,78% 100%,0 100%);display:flex;align-items:center;justify-content:center;font-size:20px;font-weight:700;line-height:1.35;text-align:center;padding:0 26px}
.hero-btn.contact{background:var(--blue-deep);width:140px;clip-path:polygon(22% 0,100% 0,100% 100%,0 100%)}
.hero-btn small{display:block;font-size:11px;font-weight:500}

/* section titles */
.section-title{text-align:center;font-size:30px;font-weight:500;color:var(--navy);letter-spacing:.05em}
.section-title::after{content:"";display:block;width:40px;height:3px;background:var(--blue);margin:14px auto 0}
.view-more{display:block;width:120px;height:34px;margin:0 auto;border:1px solid var(--blue);color:var(--blue);font-size:12px;line-height:32px;text-align:center;letter-spacing:.05em}

/* news */
.news{position:absolute;top:645px;left:0;width:1200px;height:600px;background:var(--white)}
.news .section-title{margin-top:110px}
.news-list{list-style:none;width:560px;margin:40px auto 48px}
.news-item{display:flex;align-items:center;gap:22px;height:44px;border-bottom:1px solid var(--line);font-size:14px}
.news-tag{background:var(--blue);color:var(--white);font-size:11px;padding:3px 10px}
.news-date{color:#555;width:80px}

/* booking grid */
.booking{position:absolute;top:1245px;left:0;width:1200px;height:1123px;background:var(--pale)}
.booking .section-title{margin-top:84px}
.area-grid{position:absolute;top:127px;left:0;width:1200px;display:grid;grid-template-columns:repeat(3,400px);grid-auto-rows:198px}
.area{position:relative}
.area-label{position:absolute;top:10px;left:0;background:var(--blue);color:var(--white);font-size:13px;font-weight:500;padding:4px 18px 4px 10px;clip-path:polygon(0 0,100% 0,88% 100%,0 100%)}
.a1{background:linear-gradient(180deg,#a9d4ef,#7fae5a)}
.a2{background:linear-gradient(180deg,#7cc7ef,#e1574a)}
.a3{background:linear-gradient(180deg,#c58966,#c23a2c)}
.a4{background:linear-gradient(180deg,#9fcaf0,#d96443)}
.a5{background:linear-gradient(180deg,#4a6b9e,#d84a3c)}
.a6{background:linear-gradient(180deg,#2d4a7c,#f0b45a)}
.a7{background:linear-gradient(180deg,#b9dbf2,#5c7f8e)}
.a8{background:linear-gradient(180deg,#a8c8e2,#5a4a3a)}
.a9{background:linear-gradient(180deg,#b9c9cf,#6fb0c2)}
.package-btn{position:absolute;top:860px;left:400px;width:400px;height:60px;background:var(--blue);color:var(--white);font-size:18px;font-weight:500;display:flex;align-items:center;justify-content:center;letter-spacing:.05em}

/* services */
.services{position:absolute;top:2368px;left:0;width:1200px;height:1122px;background:var(--gray-bg);overflow:hidden}
.services-shape{position:absolute;top:0;left:0;width:1200px;height:1122px}
.services .section-title{position:relative;margin-top:128px}
.service-grid{position:absolute;top:220px;left:30px;width:1140px;display:grid;grid-template-columns:repeat(3,380px);row-gap:40px}
.service{position:relative;width:360px;height:360px;border-radius:50%;margin:0 auto;display:flex;align-items:center;justify-content:center}
.service-name{position:relative;color:var(--white);font-size:26px;font-weight:500;text-align:center;line-height:1.3;text-shadow:0 2px 6px rgba(0,0,0,.35)}
.s1{background:linear-gradient(180deg,#bfe3f7,#3b8cc8 70%,#c9b48f)}
.s2{background:linear-gradient(180deg,#9ad0ef,#4b7fb3)}
.s3{background:linear-gradient(180deg,#e9edf0,#4c5560)}
.s4{background:linear-gradient(180deg,#dfe6ec,#5b6e82)}
.s5{background:linear-gradient(180deg,#c9a688,#6b4a34)}
.s6{background:linear-gradient(180deg,#d9e2ea,#3a4e6c)}
.services .view-more{position:absolute;top:995px;left:540px;background:var(--white)}

/* feature band */
.features{position:absolute;top:3490px;left:0;width:1200px;height:763px}
.feature{position:absolute;display:flex;align-items:center;justify-content:center}
.feature-label{background:rgba(60,60,60,.55);color:var(--white);font-size:20px;padding:10px 24px;letter-spacing:.08em}
.f-purpose{top:0;left:0;width:1200px;height:380px;background:linear-gradient(180deg,#3a7fc6,#a9d4f1 70%,#6a9fcf)}
.f-japan{top:380px;left:0;width:600px;height:383px;background:linear-gradient(180deg,#cfe4f3,#8aa3b8 60%,#5a6e80)}
.f-column{top:380px;left:600px;width:600px;height:383px;background:linear-gradient(135deg,#f1f1ef,#c8c2b8)}

/* faq */
.faq{position:absolute;top:4253px;left:0;width:1200px;height:562px;background:var(--white)}
.faq .section-title{margin-top:50px}
.faq-item{width:920px;margin:34px auto 0;border:1px solid var(--line);box-shadow:0 3px 8px rgba(0,0,0,.07);padding:22px 30px}
.faq-q,.faq-a{display:flex;gap:16px;font-size:15px;line-height:1.8}
.faq-q{font-weight:500;color:var(--navy);padding-bottom:12px;border-bottom:1px solid var(--line);margin-bottom:12px}
.badge{flex:0 0 28px;height:28px;border-radius:50%;background:var(--blue);color:var(--white);font-size:14px;font-weight:700;display:flex;align-items:center;justify-content:center}
.faq-a .badge{background:var(--blue-light)}

/* footer */
.site-footer{position:absolute;top:4815px;left:0;width:1200px;height:378px;background:linear-gradient(135deg,var(--blue-deep),var(--blue) 60%,#44b6f2);color:var(--white);padding:36px 48px}
.site-footer .brand{color:var(--white)}
.site-footer .brand-mark{background:var(--white)}
.footer-body{display:flex;justify-content:space-between;margin-top:34px}
.company{font-size:12px;line-height:1.9}
.company strong{font-size:15px;display:block;margin-bottom:10px}
.footer-nav{font-size:12px;line-height:2.2;text-align:right;width:560px}
.footer-nav span+span::before{content:"|";margin:0 8px}
.branch{font-size:12px;margin-top:24px}
</style>
</head>
<body>

<header class="site-header">
  <div class="brand"><span class="brand-mark"></span>ソラミチツアー</div>
  <nav class="global-nav"><a>会社概要</a><a>事業内容</a><a>ツアーの流れ</a><a>採用情報</a><a>お問合せ</a></nav>
</header>

<section class="hero">
  <div class="hero-photo" role="img" aria-label="青空を飛ぶ旅客機と南国の海辺の写真"></div>
  <svg class="hero-wedge" viewBox="0 0 1200 645" aria-hidden="true">
    <polygon points="0,645 0,540 360,645" fill="#1e9be8" opacity=".8"/>
    <polygon points="760,645 1200,520 1200,645" fill="#ffffff" opacity=".55"/>
  </svg>
  <h1 class="hero-copy">あなたの旅を<em>本気</em>で<br>サポートする会社</h1>
  <div class="hero-actions">
    <a class="hero-btn">今すぐ旅行に行く</a>
    <a class="hero-btn contact"><span>お問合せ<small>06-0000-1234</small></span></a>
  </div>
</section>

<section class="news">
  <h2 class="section-title">新着情報</h2>
  <ul class="news-list">
    <li class="news-item"><span class="news-tag">お知らせ</span><span class="news-date">2021/10/07</span>テキストテキストテキストテキストテキスト</li>
    <li class="news-item"><span class="news-tag">お知らせ</span><span class="news-date">2021/10/07</span>テキストテキストテキストテキストテキスト</li>
    <li class="news-item"><span class="news-tag">お知らせ</span><span class="news-date">2021/10/07</span>テキストテキストテキストテキストテキスト</li>
  </ul>
  <a class="view-more">VIEW MORE</a>
</section>

<section class="booking">
  <h2 class="section-title">今すぐ旅行を予約する</h2>
  <div class="area-grid">
    <div class="area a1" role="img" aria-label="北海道の丘の写真"><span class="area-label">北海道</span></div>
    <div class="area a2" role="img" aria-label="沖縄の海と獅子像の写真"><span class="area-label">沖縄</span></div>
    <div class="area a3" role="img" aria-label="京都の朱色の橋の写真"><span class="area-label">京都</span></div>
    <div class="area a4" role="img" aria-label="東京のタワーと街並みの写真"><span class="area-label">東京</span></div>
    <div class="area a5" role="img" aria-label="大阪の繁華街の写真"><span class="area-label">大阪</span></div>
    <div class="area a6" role="img" aria-label="九州の夜景の写真"><span class="area-label">九州</span></div>
    <div class="area a7" role="img" aria-label="四国の橋と海の写真"><span class="area-label">四国</span></div>
    <div class="area a8" role="img" aria-label="出雲の神社の写真"><span class="area-label">中国地方</span></div>
    <div class="area a9" role="img" aria-label="温泉の湯けむりの写真"><span class="area-label">温泉</span></div>
  </div>
  <a class="package-btn">ダイナミックパッケージへ</a>
</section>

<section class="services">
  <svg class="services-shape" viewBox="0 0 1200 1122" aria-hidden="true">
    <polygon points="0,0 300,0 0,420" fill="#ffffff" opacity=".7"/>
    <polygon points="0,0 200,0 0,260" fill="#d9d9d9"/>
  </svg>
  <h2 class="section-title">事業予約</h2>
  <div class="service-grid">
    <div class="service s1" role="img" aria-label="海辺の旅行風景の写真"><span class="service-name">ダイナミック<br>パッケージ</span></div>
    <div class="service s2" role="img" aria-label="空港と旅客機の写真"><span class="service-name">国内・海外<br>旅行</span></div>
    <div class="service s3" role="img" aria-label="出張するビジネスパーソンの写真"><span class="service-name">法人出張</span></div>
    <div class="service s4" role="img" aria-label="旅行相談の窓口の写真"><span class="service-name">プランアドバイス</span></div>
    <div class="service s5" role="img" aria-label="宴会の料理の写真"><span class="service-name">インセンティブ<br>旅行</span></div>
    <div class="service s6" role="img" aria-label="海外の街並みの写真"><span class="service-name">海外研修旅行</span></div>
  </div>
  <a class="view-more">VIEW MORE</a>
</section>

<section class="features">
  <a class="feature f-purpose" role="img" aria-label="雲の上を飛ぶ旅客機の写真"><span class="feature-label">目的別に旅行先</span></a>
  <a class="feature f-japan" role="img" aria-label="日本の都市の街並みの写真"><span class="feature-label">日本の旅行先</span></a>
  <a class="feature f-column" role="img" aria-label="ノートに書き込む手元の写真"><span class="feature-label">コラム</span></a>
</section>

<section class="faq">
  <h2 class="section-title">よくある質問</h2>
  <div class="faq-item">
    <p class="faq-q"><span class="badge">Q</span>テキストテキストテキストテキストテキストテキスト</p>
    <p class="faq-a"><span class="badge">A</span>テキストテキストテキストテキストテキストテキストテキストテキスト<br>テキストテキストテキストテキストテキストテキストテキストテキスト</p>
  </div>
  <div class="faq-item">
    <p class="faq-q"><span class="badge">Q</span>テキストテキストテキストテキストテキストテキスト</p>
    <p class="faq-a"><span class="badge">A</span>テキストテキストテキストテキストテキストテキストテキストテキスト<br>テキストテキストテキストテキストテキストテキストテキストテキスト</p>
  </div>
</section>

<footer class="site-footer">
  <div class="brand"><span class="brand-mark"></span>ソラミチツアー</div>
  <div class="footer-body">
    <div class="company">
      <strong>そらみちトラベル<br>株式会社くもたび旅行</strong>
      〒540-0000<br>
      大阪府大阪市北浜区1丁目2-3 北浜ビル5F<br>
      TEL：06-0000-1234<br>
      営業時間：平日 9:30〜18:00／土曜日 9:30〜15:00<br>
      日曜日・祝日は休業
      <p class="branch">大阪府知事登録旅行業 第2-000号</p>
    </div>
    <nav class="footer-nav">
      <p><span>TOP</span><span>会社概要</span><span>企業理念</span><span>代表あいさつ</span><span>社員紹介</span><span>プライバシーポリシー</span><span>事業内容</span></p>
      <p><span>ツアーの流れ</span><span>採用情報</span><span>目的別の旅行先</span><span>日本の旅行先</span><span>コラム</span><span>よくある質問</span><span>お客様の声</span><span>お問合せ</span></p>
    </nav>
  </div>
</footer>

</body>
</html>
```